Redesign website for small print company

Vindaborgprent is a small printing company in Iceland mainly servicing Students, schools, etc. We are also doing all kind of other jobs, like business cards, book printing, brochure printing etc. We are also selling books online.
Our website is: www.vindaborgprent.is
What we are looking for is:
- Web Design (Uncoded - PSD layout only)
- Mobile friendly design, using our current color scheme: Red, green, yellow and light gray.
- Clean simple design
- Simple, light and easy to use.
- More menu Items/drop down
Industry/Entity Type
Digital Printing
Number of Pages Required
5+ page
Requirements
Must have
- Easy navigation
- Designed for mobile
- Current color scheme (see logo)
Nice to have
- Icon based products

```html
<!DOCTYPE html>
<html lang="is">
<head>
<meta charset="utf-8">
<title>Vindaborgprent – Vörur</title>
<link rel="stylesheet" href="https://fonts.googleapis.com/css2?family=Montserrat:wght@400;500;600;700&display=swap">
<style>
:root{
  --green:#1f7a30;
  --red:#e3262c;
  --yellow:#f4c400;
  --ink:#1d1d1f;
  --muted:#444;
  --page:#e9eaee;
  --panel:#3c3d42;
  --footer:#f4f4f5;
  --white:#fff;
}
*{box-sizing:border-box;margin:0;padding:0}
html,body{width:979px;height:1200px;overflow:hidden}
body{font-family:'Montserrat',sans-serif;color:var(--ink);background:var(--white);position:relative}
.abs{position:absolute}
.topbar{left:333px;top:0;width:646px;height:38px;background:var(--green);border-bottom-left-radius:38px 38px;color:var(--white);font-weight:600;font-size:14px}
.topbar span{position:absolute;top:11px}
.social{display:inline-block;width:22px;height:22px;border:2px solid var(--white);border-radius:50%}
.brand{left:45px;top:38px;display:flex;align-items:center;gap:8px;height:44px}
.brand-mark{width:36px;height:44px;background:var(--red)}
.brand-name{font-size:22px;font-weight:600;letter-spacing:.3px;white-space:nowrap}
.nav a{position:absolute;top:61px;font-size:21px;font-weight:600;color:var(--ink);text-decoration:none}
.nav .active::after{content:"";position:absolute;left:0;right:0;top:31px;height:3px;background:var(--red)}
.page{left:0;top:102px;width:979px;height:853px;background:var(--page)}
h1{left:307px;top:152px;font-size:29px;font-weight:500}
.view-btn{left:795px;top:157px;width:79px;height:29px;border:1px solid #999;background:#f1f1f1;font-size:13px;font-weight:600;padding:6px 0 0 5px}
.sidebar{left:39px;top:196px;width:232px;height:472px;background:var(--panel);color:var(--white)}
.sidebar h2{position:absolute;left:17px;font-size:21px;font-weight:700}
.sidebar .plus{position:absolute;right:10px;width:22px;height:22px}
.sidebar .plus::before,.sidebar .plus::after{content:"";position:absolute;background:#888}
.sidebar .plus::before{left:10px;top:0;width:1px;height:22px}
.sidebar .plus::after{left:0;top:10px;width:22px;height:1px}
.sidebar ul{list-style:none;position:absolute;left:19px;top:76px;font-size:17px;font-weight:500;line-height:32.2px}
.track{left:19px;top:394px;width:200px;height:1px;background:#888}
.handle{width:14px;height:14px;background:var(--white)}
.range-label{font-size:14px;font-weight:600}
.card{background:var(--white);width:175px;text-align:center}
.card .img{width:175px}
.card .title{position:absolute;left:0;width:175px;font-size:15px;font-weight:500;line-height:18px}
.card .price{position:absolute;left:0;width:175px;font-size:13px;color:var(--muted)}
.btn-outline{left:740px;top:424px;width:91px;height:24px;background:var(--white);border:1px solid #888;font-size:13px;text-align:center;padding-top:3px}
.btn-cart{left:729px;top:461px;width:114px;height:25px;background:var(--panel);color:var(--white);font-size:13px;text-align:center;padding-top:4px}
.more{left:301px;top:779px;width:573px;height:38px;background:#dcdde1;text-align:center;font-size:14px;font-weight:600;padding-top:12px}
.footer{left:0;top:955px;width:979px;height:245px;background:var(--footer)}
.fcol{font-size:23px;font-weight:500;line-height:33px}
.fhead{font-size:23px;font-weight:700}
.footer .social{border-color:var(--ink);width:28px;height:28px}
.pay{font-size:30px;font-weight:700;color:#3a3a3a}
</style>
</head>
<body>
<header>
  <div class="abs topbar">
    <span style="left:41px">Follow us</span>
    <span style="left:137px;top:7px"><i class="social"></i> <i class="social"></i> <i class="social"></i></span>
    <svg class="abs" style="left:258px;top:8px" width="18" height="22" viewBox="0 0 18 22"><path d="M3 1 L7 1 L8 6 L5 8 Q7 13 10 16 L13 13 L17 15 L17 19 Q12 23 6 15 Q0 7 3 1Z" fill="#fff"/></svg>
    <span style="left:284px">555 0142</span>
    <svg class="abs" style="left:373px;top:6px" width="34" height="26" viewBox="0 0 34 26"><path d="M17 1 L9 9 M17 1 L25 9" stroke="#fff" stroke-width="1.5" fill="none"/><rect x="2" y="9" width="30" height="15" fill="none" stroke="#fff" stroke-width="1.5"/><text x="17" y="21" font-size="10" fill="#fff" text-anchor="middle" font-family="Montserrat,sans-serif">OPEN</text></svg>
    <span style="left:419px">Mon - Fri: 9-17</span>
    <svg class="abs" style="left:564px;top:5px" width="28" height="28" viewBox="0 0 28 28"><circle cx="14" cy="14" r="13" fill="#1f3d8c"/><path d="M1 14H27M14 1V27" stroke="#fff" stroke-width="6"/><path d="M1 14H27M14 1V27" stroke="#d42" stroke-width="3"/></svg>
    <svg class="abs" style="left:604px;top:5px" width="28" height="28" viewBox="0 0 28 28"><circle cx="14" cy="14" r="13" fill="#1f3d8c"/><path d="M1 14H27M11 1V27" stroke="#fff" stroke-width="6"/><path d="M1 14H27M11 1V27" stroke="#d42" stroke-width="3"/></svg>
  </div>
  <div class="abs brand"><div class="brand-mark"></div><div class="brand-name">VINDABORGPRENT</div></div>
  <nav class="nav">
    <a style="left:343px">Heim</a>
    <a class="active" style="left:429px">Þjónusta</a>
    <a style="left:552px">Skil á verkum</a>
    <a style="left:727px">Um okkur</a>
  </nav>
  <svg class="abs" style="left:860px;top:60px" width="28" height="28" viewBox="0 0 28 28"><circle cx="11" cy="11" r="9" fill="none" stroke="#1d1d1f" stroke-width="2.5"/><path d="M18 18 L26 26" stroke="#1d1d1f" stroke-width="3"/></svg>
  <svg class="abs" style="left:916px;top:58px" width="24" height="30" viewBox="0 0 24 30"><rect x="2" y="9" width="20" height="19" rx="2" fill="none" stroke="#1d1d1f" stroke-width="2.5"/><path d="M7 12V6a5 5 0 0 1 10 0v6" fill="none" stroke="#1d1d1f" stroke-width="2.5"/></svg>
</header>

<main class="abs page" style="top:102px"></main>
<h1 class="abs">Vörur</h1>
<div class="abs view-btn">Utsýni ≡</div>

<aside class="abs sidebar">
  <h2 style="top:22px">VÖRUFLOKKAR</h2><i class="plus" style="top:28px"></i>
  <ul><li>Nafnspjöld</li><li>Bæklingar</li><li>Ritgerðir</li><li>Kennslubækur</li><li>Bókaprentun</li><li>Veggspjöld</li></ul>
  <h2 style="top:287px">Raða</h2><i class="plus" style="top:291px"></i>
  <div style="position:absolute;left:17px;top:340px;font-size:17px;font-weight:500">Price range</div>
  <div class="abs track"></div>
  <div class="abs handle" style="left:19px;top:387px"></div>
  <div class="abs handle" style="left:203px;top:387px"></div>
  <div class="abs range-label" style="left:19px;top:409px">0 Kr</div>
  <div class="abs range-label" style="left:160px;top:409px">7000 Kr</div>
</aside>

<section>
  <div class="abs card" style="left:306px;top:227px;height:230px">
    <div class="img" role="img" aria-label="Photo of folded A3 brochures" style="height:132px;background:linear-gradient(135deg,#e6e6e6,#4a5d7a 55%,#c45a2a)"></div>
    <div class="title" style="top:156px">A3 Brotnir Bæklingar</div>
    <div class="price" style="top:192px">1.000 kr</div>
  </div>
  <div class="abs card" style="left:502px;top:227px;height:230px">
    <div class="img" role="img" aria-label="Photo of a printed wall calendar" style="height:132px;background:linear-gradient(180deg,#1e5a5a,#5aa08a 35%,#eeeeee 55%,#dddddd)"></div>
    <div class="title" style="top:155px">Dagatal 2019</div>
    <div class="price" style="top:186px">1.690 kr</div>
  </div>
  <div class="abs card" style="left:699px;top:227px;height:263px">
    <div class="img" role="img" aria-label="Photo of rolled A3 posters" style="height:116px;background:linear-gradient(180deg,#f3f3f3,#2b2b2b 55%,#dcdcdc)"></div>
    <div class="title" style="top:129px">Veggspjald A3</div>
    <div class="price" style="top:164px">1.000 kr</div>
  </div>
  <div class="abs btn-outline">Uppgötvaðu</div>
  <div class="abs btn-cart">bæta við í körfu</div>

  <div class="abs card" style="left:306px;top:501px;height:230px">
    <div class="img" role="img" aria-label="Photo of a white book with a red band" style="height:141px;background:linear-gradient(90deg,#fff 30%,#e8e8e8 45%,#f4f4f4 60%,#fff 70%)"></div>
    <div class="title" style="top:154px">Language and Thought in History</div>
    <div class="price" style="top:199px">4.900 kr</div>
  </div>
  <div class="abs card" style="left:502px;top:501px;height:230px">
    <div class="img" role="img" aria-label="Photo of a book with a colourful splash cover" style="height:141px;background:linear-gradient(90deg,#fff 30%,#e9f0e5 45%,#f2e4d8 60%,#fff 70%)"></div>
    <div class="title" style="top:154px">Skapandi Leiðir</div>
    <div class="price" style="top:199px">4.900 kr</div>
  </div>
  <div class="abs card" style="left:699px;top:501px;height:230px">
    <div class="img" role="img" aria-label="Photo of a statistics textbook with a pink title" style="height:141px;background:linear-gradient(90deg,#fff 30%,#f3dbe8 45%,#efefef 60%,#fff 70%)"></div>
    <div class="title" style="top:154px">Tölfræði í Verki</div>
    <div class="price" style="top:199px">5.990 kr</div>
  </div>
  <div class="abs more">More +</div>
</section>

<footer class="abs footer">
  <div class="abs fcol" style="left:47px;top:15px">Heim<br>Þjónusta<br>Skil á verkum<br>Um okkur</div>
  <div class="abs fhead" style="left:289px;top:5px">VÖRUFLOKKAR</div>
  <div class="abs fcol" style="left:289px;top:36px">Nafnspjöld<br>Bæklingar<br>Ritgerðir<br>Kennslubækur<br>Bókaprentun<br>Veggspjöld</div>
  <div class="abs fhead" style="left:563px;top:15px;font-weight:600">Follow us</div>
  <div class="abs" style="left:563px;top:53px"><i class="social"></i> <i class="social"></i> <i class="social"></i></div>
  <svg class="abs" style="left:564px;top:95px" width="20" height="28" viewBox="0 0 18 22"><path d="M3 1 L7 1 L8 6 L5 8 Q7 13 10 16 L13 13 L17 15 L17 19 Q12 23 6 15 Q0 7 3 1Z" fill="#1d1d1f"/></svg>
  <div class="abs" style="left:591px;top:99px;font-size:14px;font-weight:600">555 0142</div>
  <svg class="abs" style="left:565px;top:132px" width="34" height="28" viewBox="0 0 34 26"><path d="M17 1 L9 9 M17 1 L25 9" stroke="#1d1d1f" stroke-width="1.5" fill="none"/><rect x="2" y="9" width="30" height="15" fill="none" stroke="#1d1d1f" stroke-width="1.5"/><text x="17" y="21" font-size="10" fill="#1d1d1f" text-anchor="middle" font-family="Montserrat,sans-serif">OPEN</text></svg>
  <div class="abs" style="left:610px;top:137px;font-size:16px;font-weight:500">Mon - Fri: 9-17</div>
  <div class="abs" style="left:616px;top:183px;font-size:24px;font-weight:600">© 2018, Vindaborgprent</div>
  <div class="abs pay" style="left:800px;top:20px">Paynordic</div>
  <div class="abs pay" style="left:812px;top:105px;font-size:26px">Kortanet</div>
</footer>
</body>
</html>
```